"Dental Lumora" clinic needs brochure

a creative design is needed for flyer for a dental clinic, all info available on this website www.dentallumora.ae, new imagery needed.

Clinic

```html
<!DOCTYPE html>
<html lang="en">
<head>
<meta charset="utf-8">
<title>Dental Lumora – Brochure</title>
<link href="https://fonts.googleapis.com/css2?family=Montserrat:wght@300;400;700&family=Source+Sans+3:wght@400;600;700&display=swap" rel="stylesheet">
<style>
  :root{
    --teal:#1d6f7a;
    --teal-box:rgba(46,110,118,.86);
    --ink:#1b1b1b;
    --grey:#7a7a7a;
    --band-cyan:#16b9c1;
    --band-blue:#2a8fd4;
    --band-green:#2cb37b;
    --green-bar:#3cba7f;
  }
  *{margin:0;padding:0;box-sizing:border-box}
  html,body{width:1200px;height:848px;overflow:hidden;background:#fff}
  body{font-family:"Source Sans 3",sans-serif;color:var(--ink)}
  .brochure{position:relative;width:1200px;height:848px;display:flex}
  .panel{position:relative;width:400px;height:848px;overflow:hidden}

  /* left panel */
  .dentist-panel{background:linear-gradient(160deg,#f4f8fa 0%,#dfe9ee 35%,#c9dbe2 60%,#e7eef1 80%,#b9ccd4 100%)}
  .heading{font-family:"Montserrat",sans-serif;font-weight:300;letter-spacing:.5px}
  .heading b{font-weight:700;color:var(--teal)}
  .dentist-panel .heading{position:absolute;left:34px;top:28px;font-size:34px}
  .portrait{position:absolute;left:32px;top:88px;width:160px;height:160px;border-radius:50%;
    background:radial-gradient(circle at 50% 35%,#e9d3c3 0 22%,#f3f5f6 23% 55%,#2857a8 56%);border:3px solid #fff}
  .doctor{position:absolute;left:209px;top:145px}
  .doctor-name{font-weight:700;font-size:19px}
  .doctor-role{font-size:15px;color:var(--grey)}
  .bio{position:absolute;left:32px;top:278px;width:336px;height:420px;background:var(--teal-box);
    color:#fff;padding:14px 20px 0 22px;font-size:16.4px;line-height:20.6px}

  /* middle panel */
  .contact-panel{background:#fff;text-align:center}
  .brand-mark{position:absolute;left:0;right:0;top:120px;display:flex;align-items:center;justify-content:center;gap:10px;
    font-family:"Source Sans 3",sans-serif;font-weight:700;font-size:30px;color:var(--teal)}
  .brand-mark .dot{width:18px;height:18px;border-radius:50%;background:var(--teal)}
  .contact-panel .heading{position:absolute;left:0;right:0;top:304px;font-size:36px}
  .map{position:absolute;left:32px;top:376px;width:336px;height:222px;background:linear-gradient(135deg,#ecebe6,#e3e2dc 60%,#d9e4cf)}
  .address{position:absolute;left:0;right:0;top:616px;font-size:17.5px;line-height:20.8px}
  .phone{position:absolute;left:0;right:0;top:710px;display:flex;justify-content:center;align-items:center;gap:6px;
    font-weight:700;font-size:29px;color:var(--teal)}
  .web{position:absolute;left:0;right:0;top:756px;font-size:25px}
  .web b{font-weight:700}

  /* right panel */
  .logo-line{position:absolute;left:0;right:0;top:40px;display:flex;justify-content:center;align-items:center;gap:10px;
    font-weight:700;font-size:28px;color:var(--teal)}
  .logo-line .dot{width:16px;height:16px;border-radius:50%;background:var(--teal)}
  .green-bar{position:absolute;left:0;top:112px;width:400px;height:6px;background:var(--green-bar)}
  .smile-photo{position:absolute;left:0;top:118px;width:400px;height:418px;
    background:linear-gradient(120deg,#ebe9e4 0%,#e4d9cd 45%,#d9b39c 70%,#5c4438 100%)}
  .service{position:absolute;left:0;width:400px;height:94px;display:flex;align-items:center;padding-left:31px;
    color:#fff;font-family:"Montserrat",sans-serif;font-weight:300;font-size:23px;letter-spacing:.3px}
  .service b{font-weight:700;margin-left:7px}
  .service .bullet{width:12px;height:12px;border:2px solid #fff;border-radius:50%;margin-right:14px}
  .s1{top:536px;background:linear-gradient(100deg,#2a9a6f,#2f8a5e 60%,#276d4f)}
  .s2{top:632px;background:linear-gradient(100deg,#1d5d86,#1c73a0 60%,#12506f)}
  .s3{top:728px;height:96px;background:linear-gradient(100deg,#1d8f9d,#1a7e8c 60%,#12525c)}

  .band{position:absolute;bottom:0;width:400px;height:24px}
  .band.cyan{left:0;background:var(--band-cyan)}
  .band.blue{left:400px;background:var(--band-blue)}
  .band.green{left:800px;background:var(--band-green)}
</style>
</head>
<body>
<div class="brochure">
  <section class="panel dentist-panel">
    <h2 class="heading">OUR <b>DENTIST</b></h2>
    <div class="portrait" role="img" aria-label="Portrait photo of the dentist in blue scrubs"></div>
    <div class="doctor">
      <div class="doctor-name">Dr. Karim Nassar</div>
      <div class="doctor-role">Dental Surgeon</div>
    </div>
    <p class="bio">Providing the most advanced dental care in a comfortable and pleasant atmosphere are the priorities of Dr. Karim Nassar. Dr. Karim is among the most accomplished and regarded general dentists in Abu Dhabi . He is diligent in his pursuit to stay current in providing the profession’s leading dental care procedures while utilizing state of the art technology, supplies and equipment. Dr. Karim has establishing his practice more than 11 years ago. He is a graduate of Nile Valley University in Egypt and earned his bachelor degree at 2006. Dr. Karim provides quality dentistry for his patients, caring for adults and children on his practice. He is widely recognized for his thorough and gentle care of patients of all ages.</p>
  </section>

  <section class="panel contact-panel">
    <div class="brand-mark"><span class="dot"></span>Dental Lumora</div>
    <h2 class="heading">CONTACT <b>US</b></h2>
    <div class="map" role="img" aria-label="Street map showing the clinic location"></div>
    <p class="address">Suite 212, Al Rawda Crescent Road,<br>Opposite Civic Plaza<br>Abu Dhabi, UAE</p>
    <div class="phone">
      <svg width="26" height="26" viewBox="0 0 24 24" fill="none" stroke="#1d6f7a" stroke-width="1.6" aria-hidden="true"><path d="M5 3l3.5 0 1.5 4.5-2 1.5a11 11 0 0 0 7 7l1.5-2 4.5 1.5V19a2 2 0 0 1-2 2A17 17 0 0 1 3 5a2 2 0 0 1 2-2z"/></svg>
      +971 2 555 0147
    </div>
    <p class="web">www.<b>dentallumora</b>.ae</p>
  </section>

  <section class="panel services-panel">
    <div class="logo-line"><span class="dot"></span>Dental Lumora</div>
    <div class="green-bar"></div>
    <div class="smile-photo" role="img" aria-label="Photo of a smiling woman with healthy teeth"></div>
    <div class="service s1"><span class="bullet"></span>GENERAL<b>DENTISTRY</b></div>
    <div class="service s2"><span class="bullet"></span>COSMETIC<b>DENTISTRY</b></div>
    <div class="service s3"><span class="bullet"></span>BIOLOGICAL<b>DENTISTRY</b></div>
  </section>

  <div class="band cyan"></div>
  <div class="band blue"></div>
  <div class="band green"></div>
</div>
</body>
</html>
```